Flyer Advertising Summer Programs for students - 6x9 inches

We need a 6x9 front and back flyer to advertise our summer programs. We are an interfaith organization that does programs with youth of all religious and non-religious backgrounds. I've sent our logos, copy, pictures, etc. that you can work with to make it pop!

Target Market(s)

youth and their parents and religious communities

Industry/Entity Type

Non Profit

Font styles to use
Serif

Requirements
Must have
• The project needs to have a place for a mailing label and stamp and our return address. It should also include lots of pictures, our logos, be fun, and eye-catching.
Nice to have
• pictures, logo, etc.

```html
<!DOCTYPE html>
<html lang="en">
<head>
<meta charset="utf-8">
<title>Youth Summer Camp Flyer – Front and Back</title>
<link rel="stylesheet" href="https://fonts.googleapis.com/css2?family=Alfa+Slab+One&family=Roboto+Slab:wght@500;700&family=Roboto:wght@400;500&display=swap">
<style>
:root{
  --page:#f1f1f1;
  --orange:#f7a81b;
  --gold:#fbbd1a;
  --green:#3f8a35;
  --pink:#e81c63;
  --yellow:#ffe61a;
  --white:#ffffff;
  --blue:#0e6cc0;
  --blue-title:#1a56c4;
  --red:#e02532;
  --purple:#9c1c6b;
  --teal:#17b3b0;
  --violet:#7b2fa6;
  --ink:#1b1b1b;
  --muted:#8a8a8a;
}
*{box-sizing:border-box;margin:0;padding:0}
html,body{width:1200px;height:923px;overflow:hidden;background:var(--page)}
.flyer{position:absolute;top:22px;width:563px;height:842px;overflow:hidden;box-shadow:0 2px 6px rgba(0,0,0,.25)}
.flyer--front{left:26px;background:var(--orange)}
.flyer--back{left:615px;background:var(--gold)}
.shape{position:absolute;left:0;top:0}
.edge-rule{position:absolute;left:0;width:100%;height:3px;background:var(--yellow)}

/* front */
.title{position:absolute;left:62px;top:34px;width:460px;transform:rotate(-7deg);font-family:"Alfa Slab One",serif;font-weight:400;line-height:.86;-webkit-text-stroke:2px var(--white);paint-order:stroke fill;text-shadow:3px 4px 0 #222}
.title__youth{font-size:90px}
.title__summer{font-size:58px;color:var(--purple);margin-left:30px}
.title__camp{font-size:96px;margin-left:150px}
.c-blue{color:#1c79d6}.c-teal{color:var(--teal)}.c-orange{color:#f39b1d}.c-purple{color:var(--purple)}.c-green{color:#3fae3c}.c-violet{color:var(--violet)}
.trip{position:absolute;left:116px;width:300px;text-align:center;font-family:"Roboto Slab",serif;color:var(--white);line-height:1}
.trip__date{top:280px;font-size:32px;font-weight:500}
.trip__name{top:317px;font-size:23px;font-weight:700;transform:scaleX(.82)}
.trip__rule{position:absolute;left:233px;top:355px;width:86px;height:3px;background:var(--yellow)}
.trip__cost{top:372px;font-size:46px;font-weight:700;transform:scaleX(.86)}
.trip__cost b,.back-cost b{color:var(--yellow);font-weight:700}
.photo{position:absolute;top:476px;width:162px;height:112px;border-radius:14px;border:2px solid var(--white)}
.join{position:absolute;left:0;width:563px;text-align:center;font-family:"Alfa Slab One",serif;font-weight:400;line-height:1}
.join--1{top:612px;font-size:42px;color:var(--white)}
.join--2{top:668px;font-size:42px;color:var(--yellow)}
.join--3{top:721px;font-size:33px;color:var(--white)}
.join--3 span{color:var(--yellow)}
.pill-front{position:absolute;left:29px;top:776px;width:504px;height:40px;border-radius:20px;background:var(--pink);border:2px solid var(--yellow);color:var(--white);font-family:"Roboto Slab",serif;font-size:19px;font-weight:700;text-align:center;line-height:36px}

/* back */
.back-title{position:absolute;left:0;width:563px;text-align:center;color:var(--white);font-family:"Roboto Slab",serif;line-height:1}
.back-date{top:24px;font-size:38px;font-weight:500}
.back-trip{top:69px;font-size:28px;font-weight:700;transform:scaleX(.86)}
.back-rule{position:absolute;left:253px;top:110px;width:60px;height:3px;background:var(--yellow)}
.back-cost{top:121px;font-size:40px;font-weight:700;transform:scaleX(.86)}
.snap{position:absolute;width:150px;height:138px;background:var(--white);padding:8px;box-shadow:0 2px 5px rgba(0,0,0,.3)}
.snap div{width:100%;height:100%}
.info-pill{position:absolute;left:13px;top:346px;width:537px;height:46px;border-radius:23px;background:var(--blue);border:2px solid var(--white);color:var(--white);font-family:"Roboto",sans-serif;font-size:14px;line-height:18px;text-align:center;padding-top:4px}
.signup{position:absolute;left:0;width:563px;text-align:center;line-height:1}
.signup__lead{top:400px;font-family:"Roboto Slab",serif;font-size:27px;font-weight:700;color:var(--red)}
.signup__url{top:434px;font-family:"Roboto",sans-serif;font-size:18px;font-weight:500;color:var(--ink)}
.about{position:absolute;left:13px;top:462px;width:537px;height:78px;background:var(--green);border:2px solid #5ec24a;color:var(--white);font-family:"Roboto",sans-serif;font-size:14px;line-height:17.5px;padding:4px 10px;text-align:justify}
.session{position:absolute;top:550px;width:190px;text-align:center;font-family:"Alfa Slab One",serif;font-weight:400;line-height:1;-webkit-text-stroke:4px var(--white);paint-order:stroke fill}
.session__date{font-size:23px;color:var(--blue-title)}
.session__place{font-size:16px;color:var(--red);margin-top:4px;line-height:1.2}
.footer{position:absolute;left:0;top:630px;width:563px;height:212px;background:var(--purple)}
.footer__scallop{position:absolute;left:0;top:-6px;width:100%;height:12px;background:radial-gradient(circle at 6px 6px,var(--purple) 6px,transparent 6.5px) 0 0/12px 12px repeat-x}
.contact{position:absolute;left:10px;top:12px;width:280px;color:var(--white);font-family:"Roboto",sans-serif}
.contact h3{font-family:"Roboto Slab",serif;font-weight:700;font-size:12.5px;margin-bottom:4px}
.contact li{list-style:none;font-size:8.6px;line-height:11.5px;display:flex;align-items:center;gap:3px}
.contact li i{display:inline-block;width:7px;height:7px;border-radius:50%;background:var(--white)}
.partners{position:absolute;left:10px;top:122px;display:flex;gap:4px}
.partner{width:64px;height:40px;background:var(--white);border:1px solid #ddd;display:flex;align-items:center;justify-content:center;text-align:center;font-family:"Roboto",sans-serif;font-weight:500;font-size:9.5px;line-height:1.1;color:var(--blue)}
.partner--seal{width:40px;background:#7a6b5a}
.partner--seal span{width:30px;height:30px;border-radius:50%;background:#a99886}
.stamp{position:absolute;left:481px;top:14px;width:68px;height:78px;border:2px dashed var(--white);display:flex;align-items:center;justify-content:center;text-align:center;color:var(--white);font-family:"Roboto Slab",serif;font-weight:500;font-size:9px;line-height:1.3}
.mail-label{position:absolute;left:300px;top:104px;width:249px;height:90px;background:var(--white);border:2px dashed var(--purple);outline:2px solid var(--white);display:flex;align-items:center;justify-content:center;color:var(--muted);font-family:"Roboto Slab",serif;font-weight:500;font-size:11px;letter-spacing:1px}
.return-note{position:absolute;left:300px;top:16px;width:170px;color:var(--white);font-family:"Roboto Slab",serif;font-weight:500;font-size:9px;line-height:1.35;opacity:.9}
</style>
</head>
<body>

<section class="flyer flyer--front" aria-label="Flyer front">
  <svg class="shape" width="563" height="842" viewBox="0 0 563 842">
    <polygon points="0,370 140,420 281,470 420,420 563,370 563,842 0,842" fill="var(--green)"/>
    <polygon points="98,14 498,58 374,450 138,434" fill="var(--pink)"/>
    <polygon points="111,30 480,70 362,436 150,422" fill="none" stroke="var(--white)" stroke-width="1.5" stroke-dasharray="4 3"/>
  </svg>

  <h1 class="title">
    <div class="title__youth"><span class="c-blue">Y</span><span class="c-teal">o</span><span class="c-orange">u</span><span class="c-purple">t</span><span class="c-green">h</span></div>
    <div class="title__summer">summer</div>
    <div class="title__camp"><span class="c-violet">c</span><span class="c-teal">a</span><span class="c-green">m</span><span class="c-blue">p</span></div>
  </h1>

  <div class="trip trip__date">JUNE 11-16</div>
  <div class="trip trip__name">“WASHINGTON DC TRIP”</div>
  <div class="trip__rule"></div>
  <div class="trip trip__cost">COST <b>$600</b></div>

  <div class="photo" style="left:29px;background:linear-gradient(135deg,#6b5a50,#c9b3a2)" role="img" aria-label="Photo of smiling students posing together"></div>
  <div class="photo" style="left:200px;background:linear-gradient(135deg,#8a7a6e,#d8c5b3)" role="img" aria-label="Photo of three friends with arms around each other"></div>
  <div class="photo" style="left:370px;background:linear-gradient(135deg,#5a4f48,#cfc2b6)" role="img" aria-label="Photo of students waving at camp"></div>

  <div class="join join--1">JOIN BRIGHT PATH</div>
  <div class="join join--2">PARTNERS FOR AN</div>
  <div class="join join--3">INTERFAITH SUMMER<span>!!</span></div>

  <div class="pill-front">OPEN CIRCLE YOUTH LEADERSHIP INITIATIVE</div>
  <div class="edge-rule" style="top:827px"></div>
</section>

<section class="flyer flyer--back" aria-label="Flyer back">
  <svg class="shape" width="563" height="842" viewBox="0 0 563 842">
    <polygon points="0,0 563,0 563,175 430,150 281,205 140,165 0,205" fill="var(--green)"/>
    <polygon points="0,205 140,165 281,205 430,150 563,175 563,195 430,172 281,228 140,188 0,228" fill="var(--orange)"/>
  </svg>
  <div class="edge-rule" style="top:10px"></div>

  <div class="back-title back-date">JUNE 11-16</div>
  <div class="back-title back-trip">“WASHINGTON DC TRIP”</div>
  <div class="back-rule"></div>
  <div class="back-title back-cost">COST <b>$600</b></div>

  <div class="snap" style="left:32px;top:184px;transform:rotate(-8deg)"><div style="background:linear-gradient(135deg,#a23b2e,#c7c3bb)" role="img" aria-label="Photo of a large group of students outside a meditation center"></div></div>
  <div class="snap" style="left:206px;top:192px;transform:rotate(8deg)"><div style="background:linear-gradient(180deg,#a9c7e6,#6b6358)" role="img" aria-label="Photo of students cleaning up a beach"></div></div>
  <div class="snap" style="left:375px;top:180px;transform:rotate(-8deg)"><div style="background:linear-gradient(135deg,#7fa85a,#d9c8b9)" role="img" aria-label="Photo of students working together at a table"></div></div>

  <div class="info-pill">Join hundreds of other students to visit lawmakers and advocacy groups<br>through the Capitol Steps Program! &nbsp;To register, visit - www.opencircleyouth.org</div>

  <div class="signup signup__lead">To sign up, visit</div>
  <div class="signup signup__url">www.opencircleyouth.org</div>

  <p class="about">Open Circle Youth Leadership Initiative – join students from all over Los Angeles and Orange Counties for community service, leadership development, visiting various places of worship, and fun! &nbsp;You can earn a $100 college scholarship!</p>

  <div class="session" style="left:10px"><div class="session__date">July 18-20</div><div class="session__place">Westfield<br>University</div></div>
  <div class="session" style="left:186px"><div class="session__date">July 25-27</div><div class="session__place">Harbor<br>College</div></div>
  <div class="session" style="left:363px"><div class="session__date">August 1-3</div><div class="session__place">Bayview<br>State</div></div>

  <footer class="footer">
    <div class="footer__scallop"></div>
    <div class="contact">
      <h3>Bright Path Partners Contact Info</h3>
      <ul>
        <li><i></i>1480 Maple Grove Ave, Fairview, CA 90210</li>
        <li><i></i>Bright Path Partners and Open Circle Youth Leadership Initiative</li>
        <li><i></i>@BPPupdates</li>
        <li><i></i>opencirclela</li>
        <li><i></i>hello@brightpathpartners.org</li>
        <li><i></i>www.brightpathpartners.org</li>
      </ul>
    </div>
    <div class="partners">
      <div class="partner">Youth Council</div>
      <div class="partner">OCYLI</div>
      <div class="partner">Bright Path</div>
      <div class="partner partner--seal"><span></span></div>
    </div>
    <div class="return-note">Return address:<br>Bright Path Partners<br>1480 Maple Grove Ave<br>Fairview, CA 90210</div>
    <div class="stamp">PLACE<br>STAMP<br>HERE</div>
    <div class="mail-label">MAILING LABEL</div>
  </footer>
  <div class="edge-rule" style="top:833px"></div>
</section>

</body>
</html>
```